Presentation brochure La Morvane

We need a brochure presenting our training and our school. We are a building training center and have deployed our first training course on plumbing.
We already have a website as well as original illustrations which are the essence of our graphic charter.
The idea would be to take the assets made available and create a 6-page brochure, with 3 pages on the School and 3 pages on the training and its program. Attached are screenshots of the website with the information to highlight.
The creation would ideally be in shades of purple and yellow.
The design must inspire the excellence of our training and the innovation of our concept.
Design size is A4 sheet folded in 3 (i.e. 9.9 x 21 per page)
Individuals and Professional Craftsmen
Bâtiment
- Pour les titres, Aller Display

```html
<!DOCTYPE html>
<html lang="fr">
<head>
<meta charset="utf-8">
<title>La Morvane – Formation Plomberie</title>
<link rel="stylesheet" href="https://fonts.googleapis.com/css2?family=Poppins:wght@300;400;500;600;700&display=swap">
<style>
  :root{
    --purple:#5a51a8;
    --purple-dark:#4a4294;
    --lavender:#dcdaf0;
    --orange:#f2a93b;
    --peach:#fde4d4;
    --board:#dcdcdc;
    --ink:#2a2a3a;
    --soft:#f4f4f8;
    --white:#ffffff;
  }
  *{margin:0;padding:0;box-sizing:border-box}
  html,body{width:853px;height:1200px;overflow:hidden}
  body{background:var(--board);position:relative;font-family:'Poppins',sans-serif;color:var(--ink)}
  .page{position:absolute;width:302px;height:427px;background:var(--white);overflow:hidden}
  .page--cover{left:101px;top:96px}
  .page--intro{left:454px;top:179px}
  .page--details{left:69px;top:583px}
  .page--program{left:437px;top:661px;background:var(--purple)}
  .abs{position:absolute}
  .shapes{position:absolute;left:0;top:0}

  /* cover */
  .cover-photo{position:absolute}
  .cover-panel{left:159px;top:170px;width:143px;height:149px;background:var(--purple);border-radius:16px 0 0 0;padding:26px 10px 0 11px;color:var(--white)}
  .cover-title{font-size:20px;font-weight:600;line-height:1.2}
  .cover-sub{font-size:9px;font-weight:600;line-height:1.3;margin-top:12px}
  .brand{font-weight:700;color:var(--purple);letter-spacing:-.2px;white-space:nowrap}
  .brand--cover{left:30px;top:178px;font-size:15px}
  .brand--cover::before{content:"";display:block;width:20px;height:20px;border-radius:50%;background:var(--purple);margin:0 0 6px 26px}

  /* intro */
  .intro-scene{left:0;top:35px;width:302px;height:193px;background:linear-gradient(160deg,#fde8dc 0%,var(--peach) 55%,#f6d2bd 100%)}
  .intro-head{left:21px;top:12px;color:var(--white);font-weight:600;font-size:10px;line-height:1.25}
  .intro-head .duration{display:block;margin-top:12px;font-size:10.5px;width:80px}
  .intro-text{left:21px;top:254px;width:225px;font-size:6.4px;font-weight:300;color:var(--purple);text-transform:uppercase;line-height:1.32}

  .footer-label{font-size:4.8px;font-weight:600;color:var(--purple);line-height:1.25}
  .footer-brand{font-size:6px}

  /* details */
  .details-title{left:21px;top:24px;width:240px;font-size:9.8px;font-weight:600;color:var(--purple);line-height:1.25}
  .details-body{left:21px;top:61px;width:118px;font-size:4.7px;line-height:1.3}
  .details-body p+p{margin-top:6px}
  .details-art{left:148px;top:68px;width:134px;height:84px;border-radius:4px;background:linear-gradient(135deg,#fbe1c8 0%,#f6c27a 45%,#b3aee0 100%)}
  .outcomes-title{left:21px;top:195px;font-size:9.5px;font-weight:600;color:var(--white)}
  .outcomes{left:21px;top:222px;width:262px;display:grid;grid-template-columns:1fr 1fr;column-gap:14px}
  .checklist{list-style:none}
  .checklist li{position:relative;padding-left:10px;font-size:4.7px;font-weight:300;line-height:1.25;margin-bottom:6px}
  .checklist li::before{content:"";position:absolute;left:0;top:.5px;width:5px;height:5px;border:.6px solid currentColor;border-radius:50%;opacity:.8}
  .checklist li::after{content:"";position:absolute;left:1.6px;top:1.6px;width:2.6px;height:1.4px;border-left:.6px solid currentColor;border-bottom:.6px solid currentColor;transform:rotate(-45deg)}
  .on-purple{color:var(--white)}
  .info-area{left:0;top:303px;width:181px;height:124px;background:var(--soft)}
  .info{left:21px;top:311px;width:260px;display:grid;grid-template-columns:78px 1fr;column-gap:3px}
  .info-item{position:relative;padding-left:10px;margin-bottom:9px}
  .info-item h4{font-size:4.4px;font-weight:600;line-height:1.3}
  .info-item p{font-size:3.5px;font-weight:300;color:#777;line-height:1.35;margin-top:2px}
  .info-item svg{position:absolute;left:0;top:0}

  /* program */
  .program-title{left:22px;top:20px;font-size:10px;font-weight:600;color:var(--white)}
  .program-list{left:22px;top:40px;width:240px}
  .program-list .checklist li{font-size:4.5px;margin-bottom:7px}
  .program-sub{font-size:5.3px;font-weight:600;color:var(--white);margin:2px 0 8px}
  .program-art{left:15px;top:210px;width:287px;height:167px;background:linear-gradient(135deg,#6b63b8 0%,#8f89cf 40%,#f2b04a 100%);border-radius:4px 0 0 4px}
  .program-footer{left:0;top:392px;width:302px;height:35px;background:var(--white)}
</style>
</head>
<body>

<!-- Cover -->
<section class="page page--cover">
  <svg class="shapes" width="302" height="427" viewBox="0 0 302 427">
    <polygon points="0,0 302,0 302,170 0,108" fill="#8f8f93" role="img" aria-label="Photo of a training plumbing installation with pipes and a toilet"/>
    <polygon points="0,222 302,262 302,427 0,427" fill="#c9c4bb" role="img" aria-label="Photo of the training workshop with plasterboard booths and benches"/>
    <polygon points="0,365 0,427 200,427" fill="var(--lavender)"/>
    <polygon points="0,398 0,427 70,427" fill="#ffffff" opacity=".6"/>
  </svg>
  <div class="abs brand brand--cover">La Morvane</div>
  <div class="abs cover-panel">
    <h1 class="cover-title">Formation Plomberie</h1>
    <p class="cover-sub">Maitrisez les fondamentaux de Plomberie en seulement 1 semaine !</p>
  </div>
</section>

<!-- Intro -->
<section class="page page--intro">
  <div class="abs intro-scene" role="img" aria-label="Illustration of two apprentices working at a sink in a training booth"></div>
  <svg class="shapes" width="302" height="140" viewBox="0 0 302 140">
    <path d="M0,0 H200 L102,86 Q88,98 70,94 L0,70 Z" fill="var(--purple)"/>
  </svg>
  <h2 class="abs intro-head">Formation Plomberie<span class="duration">Temps plein (1 semaine)</span></h2>
  <p class="abs intro-text">En une semaine de formation intensive mélangeant théorie en digital et pratique sur notre campus encadré par un artisan professionnel, apprenez toutes les compétences d'un plombier pour vous lancer dans vos travaux ou changer de carrière.</p>
  <p class="abs footer-label" style="left:21px;top:408px">Formation<br>Plomberie</p>
  <p class="abs brand footer-brand" style="left:256px;top:410px">La Morvane</p>
</section>

<!-- Details -->
<section class="page page--details">
  <h2 class="abs details-title">Maitrisez les fondamentaux de Plomberie en seulement 1 semaine !</h2>
  <div class="abs details-body">
    <p>Les formations de plomberie sont longues et couteuses. La Morvane a construit un programme intense qui va a l'essentiel pour les débutants comme pour les artisans confirmés. Notre secret ? Nous avons déporté toute la partie théorique via un apprentissage ludique en mobile learning :</p>
    <p>de courtes videos accessibles partout, de la gamification pour se tester et des fiches essentielles pour mémoriser les notions fondamentales.</p>
    <p>La semaine que vous passerez sur notre campus sera donc consacrée quasi exclusivement a la pratique ou vous serez encadré par un artisan professionnel. Notre communauté de Morvaneurs grandit vite. Venez vivre une expérience unique !</p>
  </div>
  <div class="abs details-art" role="img" aria-label="Illustration of plumbing tools, measuring instruments and learning apps"></div>
  <svg class="shapes" width="302" height="427" viewBox="0 0 302 427">
    <path d="M0,184 L280,172 Q302,171 302,192 V303 H0 Z" fill="var(--purple)"/>
  </svg>
  <h3 class="abs outcomes-title">A l'issue de cette formation, vous serez capable de</h3>
  <div class="abs outcomes on-purple">
    <ul class="checklist">
      <li>Identifier les éléments d'une installation de plomberie</li>
      <li>Travailler le cuivre : brasure, cintrage, réalisation de collets battus, baionnettes,</li>
      <li>Monter un appareil sanitaire raccordé a l'alimentation et a l'évacuation</li>
      <li>Modifier une installation sanitaire existante (arrivée d'eau, lavabo, machine a laver)</li>
    </ul>
    <ul class="checklist">
      <li>Réaliser l'installation d'un réseau d'eau chaude sanitaire via le montage d'un ballon d'eau chaude sanitaire et de ses accessoires</li>
      <li>Diagnostiquer un dysfonctionnement sur un réseau sanitaire et y remédier</li>
      <li>Réaliser la maintenance courante, préventive et améliorative des équipements</li>
      <li>Intégrer les principes de développement durable</li>
    </ul>
  </div>
  <div class="abs info-area"></div>
  <div class="abs info">
    <div>
      <div class="info-item"><svg width="7" height="6" viewBox="0 0 7 6"><circle cx="2.2" cy="1.6" r="1.3" fill="var(--purple)"/><circle cx="5" cy="1.6" r="1.1" fill="var(--purple)"/><path d="M0,6 Q2.2,2.6 4.4,6Z M3.4,6 Q5,3 7,6Z" fill="var(--purple)"/></svg><h4>Public :</h4><p>Particulier et professionnel</p></div>
      <div class="info-item"><svg width="6" height="6" viewBox="0 0 6 6"><circle cx="3" cy="3" r="2.5" fill="none" stroke="var(--purple)" stroke-width=".9"/><path d="M3,1.5V3H4.2" stroke="var(--purple)" stroke-width=".7" fill="none"/></svg><h4>Durée formation :</h4><p>1 semaine(s)</p></div>
      <div class="info-item"><svg width="5" height="7" viewBox="0 0 5 7"><path d="M2.5,7 C0,4 0,3.5 0,2.5 A2.5,2.5 0 0 1 5,2.5 C5,3.5 5,4 2.5,7Z" fill="var(--purple)"/><circle cx="2.5" cy="2.5" r=".9" fill="#fff"/></svg><h4>Lieu :</h4><p>Campus Est (Val-Morin)</p></div>
      <div class="info-item"><svg width="6" height="6" viewBox="0 0 6 6"><rect x=".4" y="1" width="5.2" height="4.6" fill="none" stroke="var(--purple)" stroke-width=".8"/><rect x=".4" y="1" width="5.2" height="1.3" fill="var(--purple)"/></svg><h4>Sessions :</h4><p>26 Octobre 2022</p></div>
    </div>
    <div>
      <div class="info-item"><svg width="6" height="6" viewBox="0 0 6 6"><path d="M0,3 L3,0 H6 V3 L3,6Z" fill="var(--purple)"/><circle cx="4.5" cy="1.5" r=".6" fill="#fff"/></svg><h4>Tarif :</h4><p>1890 €</p></div>
      <div class="info-item"><svg width="6" height="6" viewBox="0 0 6 6"><rect x="0" y="1.5" width="6" height="4.5" rx=".6" fill="var(--purple)"/><rect x="2" y=".3" width="2" height="1.4" fill="none" stroke="var(--purple)" stroke-width=".6"/></svg><h4>Prérequis :</h4><p>Maitrise du français (lu, écrit, parlé), opérations de calcul de base, bonne condition physique générale</p></div>
      <div class="info-item"><svg width="6" height="6" viewBox="0 0 6 6"><path d="M1,5 L4,2" stroke="var(--purple)" stroke-width="1.2"/><circle cx="4.5" cy="1.5" r="1.3" fill="var(--purple)"/></svg><h4>Équipements nécessaires :</h4><p>Chaussures de sécurité et gants de soudure</p></div>
      <div class="info-item"><svg width="5" height="6" viewBox="0 0 5 6"><rect x=".3" y=".3" width="4.4" height="5.4" fill="none" stroke="var(--purple)" stroke-width=".6"/><path d="M1.2,2H3.8M1.2,3.2H3.8M1.2,4.4H3" stroke="var(--purple)" stroke-width=".5"/></svg><h4>Programme détaillé :</h4><p style="color:var(--purple)">Téléchargez le programme</p></div>
    </div>
  </div>
  <p class="abs footer-label" style="left:21px;top:408px">Formation<br>Plomberie</p>
  <p class="abs brand footer-brand" style="left:256px;top:410px">La Morvane</p>
</section>

<!-- Program -->
<section class="page page--program">
  <svg class="shapes" width="302" height="110" viewBox="0 0 302 110">
    <polygon points="263,0 302,0 302,98" fill="#ffffff"/>
    <polygon points="288,0 302,0 302,30" fill="var(--lavender)"/>
  </svg>
  <h2 class="abs program-title">Téléchargez le programme</h2>
  <div class="abs program-list on-purple">
    <ul class="checklist">
      <li>Intégrer les principes de développement durable</li>
      <li>Réaliser l'installation complete d'une salle de bain : montage d'un lavabo, d'une douche, d'un WC, raccordement via multicouche, cuivre, PER et évacuation en PVC</li>
    </ul>
    <p class="program-sub">Vous aurez également acquis un savoir considérable et connaitrez :</p>
    <ul class="checklist">
      <li>Les principales normes en vigueur du DTU 60</li>
      <li>Les notions essentielles sur l'eau</li>
      <li>Les notions d'étancheité, d'évacuation et les bases pour l'installation d'un appareil sanitaire</li>
      <li>Les propriétés et regles d'installation du cuivre, du PER, du multicouche et du PVC</li>
      <li>Les moyens de production d'eau chaude sanitaire</li>
      <li>Et bien plus encore</li>
    </ul>
    <p class="program-sub">Vous obtiendrez a l'issue de votre formation :</p>
    <ul class="checklist">
      <li>Attestation de fin de formation</li>
    </ul>
  </div>
  <div class="abs program-art" role="img" aria-label="Illustration of learners following the course online on laptops and screens"></div>
  <div class="abs program-footer"></div>
  <p class="abs footer-label" style="left:22px;top:404px">Formation<br>Plomberie</p>
  <p class="abs brand footer-brand" style="left:256px;top:406px">La Morvane</p>
</section>

</body>
</html>
```